Business Card Design

Buy and sell properties
Buy and rehab properties
Buy properties for cash
That is what I do but do need a logo
looking for some type of logo or design on it
Just started business
Back of card should say something like BUY HOUSES CASH
Overview: it is a new company. Basically I buy properties wholesale and fix them up and sell them or sell them to other fix and flippers
Background: company is new so not any background
Market: is basically anyone selling a house or buying a house. Someone that needs to sell house fast. Basically I am a cash home buyer!!!

Updates
Email on card should be:   harborlanerealtyinc@mailbox.test

Industry/Entity Type
House
Contact Information for Business Card
Harbor Lane Realty Inc
PO Box 718269
Cedar Marsh FL 32987

Dale Morrick
dmorrick@mailbox.test
555-271-6094

```html
<!DOCTYPE html>
<html lang="en">
<head>
<meta charset="utf-8">
<title>Harbor Lane Realty Inc — Business Card</title>
<link rel="stylesheet" href="https://fonts.googleapis.com/css2?family=Montserrat:wght@400;500;600;700&display=swap">
<style>
  :root {
    --backdrop: #737373;
    --card: #ffffff;
    --brand-blue: #0d5fb0;
    --brand-grey: #7b7d80;
    --band-grey: #55575b;
    --ink: #2a2a2a;
  }
  * { box-sizing: border-box; margin: 0; padding: 0; }
  html, body { width: 1200px; height: 1000px; overflow: hidden; }
  body {
    background: var(--backdrop);
    font-family: "Montserrat", sans-serif;
    position: relative;
  }
  .card {
    position: absolute;
    width: 600px;
    height: 343px;
    background: var(--card);
    overflow: hidden;
    box-shadow: 0 6px 14px rgba(0,0,0,0.25);
  }
  .card--front { left: 220px; top: 100px; }
  .card--back  { left: 410px; top: 545px; }

  /* Front */
  .lockup {
    position: absolute;
    left: 70px;
    top: 122px;
    display: flex;
    align-items: center;
    gap: 16px;
  }
  .lockup__dot {
    width: 34px; height: 34px;
    border-radius: 50%;
    background: var(--brand-blue);
    flex: none;
  }
  .lockup__name {
    font-size: 30px;
    font-weight: 500;
    color: var(--brand-grey);
    line-height: 1;
    white-space: nowrap;
  }
  .lockup__tagline {
    margin-top: 8px;
    font-size: 19px;
    font-weight: 400;
    letter-spacing: 0.5px;
    color: var(--brand-blue);
    text-align: right;
  }

  /* Back */
  .person { position: absolute; left: 50px; top: 60px; }
  .person__name { font-size: 19px; font-weight: 700; color: var(--brand-blue); }
  .person__role { font-size: 12px; color: var(--ink); margin-top: 4px; }

  .lockup--small { left: auto; right: 40px; top: 58px; gap: 9px; }
  .lockup--small .lockup__dot { width: 18px; height: 18px; }
  .lockup--small .lockup__name { font-size: 17px; }
  .lockup--small .lockup__tagline { font-size: 11px; margin-top: 4px; }

  .contact {
    position: absolute;
    left: 50px;
    top: 148px;
    font-size: 15px;
    color: var(--ink);
    list-style: none;
  }
  .contact__item { display: flex; align-items: center; gap: 8px; margin-bottom: 5px; }
  .contact__item svg { width: 15px; height: 15px; fill: var(--brand-blue); flex: none; }
  .contact__address { margin-top: 6px; font-size: 16px; line-height: 1.4; }

  .bands { position: absolute; left: 0; bottom: 0; width: 600px; height: 60px; }
</style>
</head>
<body>

  <section class="card card--front" aria-label="Card front">
    <div class="lockup">
      <span class="lockup__dot"></span>
      <div>
        <div class="lockup__name">Harbor Lane Realty Inc</div>
        <div class="lockup__tagline">BUY HOUSES CASH</div>
      </div>
    </div>
  </section>

  <section class="card card--back" aria-label="Card back">
    <div class="person">
      <div class="person__name">Dale Morrick</div>
      <div class="person__role">Director</div>
    </div>

    <div class="lockup lockup--small">
      <span class="lockup__dot"></span>
      <div>
        <div class="lockup__name">Harbor Lane Realty Inc</div>
        <div class="lockup__tagline">BUY HOUSES CASH</div>
      </div>
    </div>

    <ul class="contact">
      <li class="contact__item">
        <svg viewBox="0 0 16 16" aria-hidden="true"><path d="M2 6c0-2 2.5-3 6-3s6 1 6 3v1h-3V5.5H5V7H2z"/><path d="M4 8h8l2 5H2z"/></svg>
        <span>555.271.6094</span>
      </li>
      <li class="contact__item">
        <svg viewBox="0 0 16 16" aria-hidden="true"><path d="M1 3h14v10H1z" /><path d="M1.5 3.5 8 9l6.5-5.5" fill="none" stroke="#fff" stroke-width="1.3"/></svg>
        <span>harborlanerealtyinc@mailbox.test</span>
      </li>
      <li class="contact__address">PO Box 718269 Cedar Marsh<br>FL 32987</li>
    </ul>

    <svg class="bands" viewBox="0 0 600 60" aria-hidden="true">
      <polygon points="0,26 375,26 369,60 0,60" fill="var(--band-grey)"/>
      <path d="M390,12 Q392,4 402,4 L600,4 L600,60 L382,60 Z" fill="var(--brand-blue)"/>
    </svg>
  </section>

</body>
</html>
```